Kestrel Business Accountants , logo & business card design

I am a business consultant & accountant , servicing a range of small business clients , providing business & taxation advice.
I am looking for a logo & business card design that is not traditional accounting style.
Something colorful & innovative would be good.
Target Market(s)
Small businesses in their growth stage
Industry/Entity Type
Business Consultant
Contact Information for Business Card
Kestrel Business Accountants Pty Ltd
Miles Hartley CPA
Director
Ph: 0413 8064 91
Email : kestrel@pallinet.com.au
On reverse of card:
"Kestrel Sight for your Business"
Business Consulting
Taxation
Superannuation
Logo styles of interest
Abstract Logo
Wordmark Logo
Look and feel

```html
<!DOCTYPE html>
<html lang="en">
<head>
<meta charset="utf-8">
<title>Kestrel Business Accountants – Business Card</title>
<link href="https://fonts.googleapis.com/css2?family=Orbitron:wght@400;500;700;800&display=swap" rel="stylesheet">
<style>
  :root {
    --backdrop: #e2e2e2;
    --card: #1e1e1e;
    --lime: #7ac943;
    --silver: #a3a3a3;
    --shadow: rgba(0, 0, 0, 0.28);
  }
  * { margin: 0; padding: 0; box-sizing: border-box; }
  html, body {
    width: 1200px;
    height: 900px;
    overflow: hidden;
    background: var(--backdrop);
  }
  .sheet {
    position: relative;
    width: 1200px;
    height: 900px;
    display: flex;
    align-items: center;
    justify-content: center;
    gap: 40px;
  }
  .card {
    width: 520px;
    height: 318px;
    background: var(--card);
    box-shadow: 0 10px 24px var(--shadow);
    display: flex;
    flex-direction: column;
    align-items: center;
    justify-content: center;
    text-align: center;
    font-family: "Orbitron", sans-serif;
    text-transform: uppercase;
  }

  /* Front */
  .wordmark {
    color: var(--silver);
    font-weight: 700;
    line-height: 1.15;
  }
  .wordmark--large .wordmark__name { font-size: 44px; letter-spacing: 2px; }
  .wordmark--large .wordmark__sub { font-size: 12px; letter-spacing: 1.5px; }
  .wordmark--large .wordmark__legal { font-size: 8px; letter-spacing: 2px; }
  .front__rule {
    width: 250px;
    height: 1px;
    background: var(--silver);
    margin: 8px 0 12px;
  }
  .tagline {
    color: var(--lime);
    font-weight: 700;
    font-size: 12px;
    letter-spacing: 0.8px;
  }
  .services {
    color: var(--silver);
    font-size: 10px;
    letter-spacing: 1.2px;
    margin-top: 4px;
  }

  /* Back */
  .person__name {
    color: var(--lime);
    font-weight: 800;
    font-size: 24px;
    letter-spacing: 1.5px;
  }
  .person__role {
    color: var(--silver);
    font-size: 10px;
    letter-spacing: 1.2px;
    margin-top: 3px;
  }
  .contact { margin-top: 12px; }
  .contact__label {
    color: var(--lime);
    font-weight: 700;
    font-size: 11px;
    letter-spacing: 1px;
    margin-top: 6px;
  }
  .contact__value {
    color: var(--silver);
    font-size: 15px;
    letter-spacing: 1px;
    text-transform: none;
  }
  .contact__value--email { text-transform: uppercase; font-size: 14px; }
  .wordmark--small { margin-top: 18px; }
  .wordmark--small .wordmark__name { font-size: 18px; letter-spacing: 1px; }
  .wordmark--small .wordmark__sub { font-size: 6px; letter-spacing: 0.6px; }
  .wordmark--small .wordmark__legal { font-size: 4.5px; letter-spacing: 1px; }
</style>
</head>
<body>
  <main class="sheet">
    <section class="card card--front" aria-label="Card front">
      <div class="wordmark wordmark--large">
        <div class="wordmark__name">Kestrel</div>
        <div class="wordmark__sub">Business Accountants</div>
        <div class="wordmark__legal">Pty Ltd</div>
      </div>
      <div class="front__rule"></div>
      <p class="tagline">“Kestrel Sight for your Business”</p>
      <p class="services">Business Consulting Taxation Superannuation</p>
    </section>

    <section class="card card--back" aria-label="Card back">
      <h1 class="person__name">Miles Hartley</h1>
      <p class="person__role">CPA Director</p>
      <div class="contact">
        <p class="contact__label">Ph:</p>
        <p class="contact__value">0413 8064 91</p>
        <p class="contact__label">Email:</p>
        <p class="contact__value contact__value--email">kestrel@pallinet.com.au</p>
      </div>
      <div class="wordmark wordmark--small">
        <div class="wordmark__name">Kestrel</div>
        <div class="wordmark__sub">Business Accountants</div>
        <div class="wordmark__legal">Pty Ltd</div>
      </div>
    </section>
  </main>
</body>
</html>
```